Wedding design templates - fresh

We require 3 different wedding designs. I have attached the watercolour images for the graphic designer to use on each template. I want to be able to easily change the name and location of the invitation when needed and be able to freely use whatever font is used, so that the invite becomes our template. I want something fresh with a modern layout but on a white background. The use of coloured fonts are okay to suit the images provided. The size of the card stock is A5 (half of an A4) please consider bleeds etc for printing.

Target Market(s)

Bridal market - young couples

Industry/Entity Type

Wedding

Font styles to use
Serif
Sans Serif
Script

Requirements
Must have
• Be able to use fonts and change details easily. common colours that can easily fit in with a brides colour scheme. must have all details for wedding invites ie church name address etc can be any church or reception place in sydney
Nice to have
• i have uploaded some example images as to style i am looking for.
• I want to be able to run a theme with these images eg. rsvp cards, place cards etc

```html
<!DOCTYPE html>
<html lang="en">
<head>
<meta charset="utf-8">
<title>Wedding Invitation – Sophie &amp; Lucas</title>
<link href="https://fonts.googleapis.com/css2?family=Pinyon+Script&family=Tinos:ital@1&display=swap" rel="stylesheet">
<style>
  :root {
    --page: #ffffff;
    --ink-script: #5b5f7c;
    --ink-caps: #5f6378;
    --ink-body: #1f1f24;
    --ampersand: #ddbcae;
    --petal-pink: #f1d9d4;
    --petal-cream: #f4efd2;
    --leaf-green: #b9cda4;
    --umbel: #dfe8d8;
  }
  * { margin: 0; padding: 0; box-sizing: border-box; }
  html, body { width: 835px; height: 1200px; overflow: hidden; background: var(--page); }
  .invitation {
    position: absolute; left: 32px; top: 55px; width: 771px; height: 1090px;
    background: var(--page);
    box-shadow: 0 0 6px rgba(0,0,0,.35);
    overflow: hidden;
  }
  .floral {
    position: absolute; border-radius: 50%;
  }
  .floral--top-left { left: 0; top: 0; width: 150px; height: 220px;
    background: radial-gradient(ellipse at 40% 30%, var(--petal-pink) 0%, rgba(241,217,212,.5) 40%, rgba(223,232,216,.5) 70%, transparent 85%); }
  .floral--top-right { right: 0; top: 0; width: 190px; height: 110px;
    background: radial-gradient(ellipse at 60% 40%, var(--umbel) 0%, rgba(223,232,216,.6) 50%, transparent 80%); }
  .floral--bottom-right { right: 0; top: 680px; width: 210px; height: 420px; border-radius: 45% 0 0 45%;
    background: radial-gradient(ellipse at 55% 45%, var(--petal-cream) 0%, var(--petal-pink) 35%, rgba(185,205,164,.7) 65%, transparent 88%); }
  .floral--bottom-strip { left: 110px; bottom: 0; width: 560px; height: 90px; border-radius: 50% 50% 0 0;
    background: radial-gradient(ellipse at 50% 80%, var(--petal-pink) 0%, rgba(244,239,210,.7) 45%, rgba(223,232,216,.5) 70%, transparent 90%); }

  .line { position: absolute; left: 0; width: 100%; text-align: center; }
  .script { font-family: "Pinyon Script", cursive; color: var(--ink-script); }
  .caps { font-family: "Tinos", serif; font-style: italic; text-transform: uppercase; color: var(--ink-caps); font-size: 15px; }
  .body { font-family: "Tinos", serif; font-style: italic; color: var(--ink-body); font-size: 20px; }
  .small { font-size: 14px; color: var(--ink-body); }

  .hosts { top: 92px; font-size: 25px; }
  .together { top: 138px; }
  .cohost { top: 170px; font-size: 23px; }
  .request { top: 235px; }
  .guests { top: 268px; font-size: 36px; }
  .celebrate { top: 328px; }

  .couple { position: absolute; left: 0; top: 340px; width: 100%; height: 220px; }
  .couple__amp { position: absolute; left: 300px; top: 0; font-family: "Pinyon Script", cursive;
    font-size: 210px; line-height: 1; color: var(--ampersand); }
  .couple__name { position: absolute; font-family: "Pinyon Script", cursive; color: var(--ink-script); font-size: 46px; line-height: 1; white-space: nowrap; }
  .couple__name--bride { left: 150px; top: 60px; }
  .couple__name--groom { left: 352px; top: 116px; }

  .venue { top: 573px; line-height: 26px; }
  .date { top: 683px; font-size: 33px; }
  .date sup { font-size: 16px; }
  .after { top: 756px; }
  .fill-line { top: 780px; font-size: 14px; letter-spacing: 1px; color: var(--ink-body); }
  .street { top: 815px; }
  .dinner { top: 838px; }
  .rsvp { top: 909px; line-height: 25px; }
</style>
</head>
<body>
  <main class="invitation">
    <div class="floral floral--top-left" role="img" aria-label="Watercolour pink anemone with white umbel flowers"></div>
    <div class="floral floral--top-right" role="img" aria-label="Watercolour white umbel flower sprigs"></div>
    <div class="floral floral--bottom-right" role="img" aria-label="Watercolour cluster of pink and cream anemones with leaves"></div>
    <div class="floral floral--bottom-strip" role="img" aria-label="Watercolour border of anemones and umbel flowers"></div>

    <p class="line script hosts">Helen and Mark Carter</p>
    <p class="line caps together">Together with</p>
    <p class="line script cohost">Pieter De Vries</p>
    <p class="line caps request">Request the pleasure of</p>
    <p class="line script guests">Helen, Mark &amp; Liam</p>
    <p class="line caps celebrate">To celebrate the marriage of</p>

    <div class="couple">
      <span class="couple__amp" aria-hidden="true">&amp;</span>
      <span class="couple__name couple__name--bride">Sophie Carter</span>
      <span class="couple__name couple__name--groom">Lucas de Vries</span>
    </div>

    <p class="line body venue">St Aidan's Chapel<br>58 Harbour Lane<br>Glenmore NSW 2099</p>
    <p class="line script date">on Saturday 7<sup>th</sup> December at 3pm</p>
    <p class="line caps small after">And afterwards at</p>
    <p class="line fill-line">...........................................</p>
    <p class="line caps small street">...................Street</p>
    <p class="line caps small dinner">For dinner and dancing</p>
    <p class="line caps small rsvp">RSVP by 7th October<br>Sophie 010 000 0000</p>
  </main>
</body>
</html>
```